Redesign wellness clinic website

The project is redesign a wellness clinic http://www.thornleighvitality.example. The new website is to be responsive,clean,bright and a strong call to action which is to book an appointment. The logo will remain the same but the colour scheme on the website should be reflect purple white and green. I want it to be bright and cheerful and the feeling of clarity. The website shouldn't be overloaded with content but more visuals.

Target Market(s)

Anyone that has corporate wellness benefits within the downtown Toronto core. Majority of audience are professional working in Media, Telecommunications and Investments.

Industry/Entity Type

Health And Wellness

Number of Pages Required

5+ page

Font styles to use
Sans Serif

Colors
ffffff
886aae
acd036

Requirements
Must have
• -Strong call to action which is book an appointment like this page https://www.kestrelmotion.example/
• -Services provided icons on the page like https://www.brightpathvitalityhouse.example/
• - Pictures of a good visualizing a fit and healthy life
• - Strong ratings from Quorva, Zintrel, PostMaz, similar to this website http://www.summitbalancehealth.example/our-team-professionals/
• - Bright and clear
Should not have
• -No black and white images (redo our pictures)
• -Dark themes

```html
<!DOCTYPE html>
<html lang="en">
<head>
<meta charset="utf-8">
<title>News &amp; Updates – Thornleigh Vitality Centre</title>
<link href="https://fonts.googleapis.com/css2?family=Fira+Sans:wght@400;500;600&display=swap" rel="stylesheet">
<style>
:root{
  --purple:#886aae;
  --purple-dark:#7a5ea1;
  --green:#acd036;
  --green-dark:#9cc02a;
  --orange:#f08a24;
  --ink:#2c2c2c;
  --body:#555;
  --muted:#8a8a8a;
  --rule:#e3e3e3;
  --band:#f1f1f1;
  --white:#ffffff;
}
*{box-sizing:border-box;margin:0;padding:0}
html,body{width:1200px;height:2752px;overflow:hidden}
body{position:relative;background:var(--white);font-family:"Fira Sans",Arial,sans-serif;color:var(--body)}
a{color:inherit;text-decoration:none}

/* header */
.brand{position:absolute;left:172px;top:26px;display:flex;align-items:center;gap:10px}
.brand-dot{width:40px;height:40px;border-radius:50%;background:var(--purple)}
.brand-name{font-size:13px;font-weight:600;color:var(--purple);line-height:1.2}
.brand-name small{display:block;font-size:10px;font-weight:400;color:var(--green-dark)}
.header-cta{position:absolute;top:28px;right:172px;display:flex;gap:12px}
.pill{height:37px;border-radius:19px;color:var(--white);font-size:13px;font-weight:500;display:flex;align-items:center;justify-content:center;gap:8px}
.pill-call{width:180px;background:var(--green)}
.pill-book{width:186px;background:var(--purple)}
.pill svg{width:13px;height:13px}

/* nav */
.main-nav{position:absolute;left:0;top:92px;width:1200px;height:36px;background:var(--band)}
.main-nav ul{list-style:none;position:absolute;left:172px;top:0;display:flex;height:36px}
.main-nav li{font-size:12.5px;color:#444;line-height:36px;padding:0 10px}
.main-nav li.is-active{background:var(--green);color:var(--white)}
.search{position:absolute;right:172px;top:6px;width:169px;height:24px;border-radius:12px;background:var(--white);font-size:12px;color:#aaa;display:flex;align-items:center;gap:7px;padding-left:14px}

/* hero */
.hero{position:absolute;left:0;top:128px;width:1200px;height:298px}
.hero svg{position:absolute;left:0;top:0}
.hero-title{position:absolute;left:261px;top:70px;width:170px;text-align:center}
.hero-title span{display:block;width:44px;height:44px;margin:0 auto 14px;border:3px solid var(--purple);border-radius:50%}
.hero-title h1{font-size:22px;font-weight:500;color:var(--purple)}

/* posts */
.posts{position:absolute;left:172px;top:464px;width:856px}
.post{height:346px}
.post-date{font-size:12px;color:var(--muted);line-height:18px}
.post-title{font-size:17px;font-weight:500;color:var(--ink);line-height:22px;padding-bottom:10px;border-bottom:1px solid var(--rule)}
.post-body{display:flex;gap:22px;margin-top:21px}
.post-photo{width:344px;height:226px;flex:none}
.post-text{font-size:13px;line-height:19.5px;color:var(--body)}
.post-text p+p{margin-top:20px}
.learn-more{display:inline-block;margin-top:8px;font-size:12px;color:var(--purple);font-weight:500}
.photo-yoga{background:linear-gradient(160deg,#f3d9a0,#c9a25a 45%,#6f7a2e)}
.photo-rehab{background:linear-gradient(120deg,#eef0f2,#c9d3dc 40%,#f0a860 60%,#7a8a9c)}
.photo-gym{background:linear-gradient(110deg,#f6e7c8,#c9a27a 40%,#4b4b52)}
.photo-stretch{background:linear-gradient(120deg,#e3d9cc,#c7b6a4 40%,#e76f4f 60%,#8f8a86)}
.photo-run{background:linear-gradient(150deg,#fbe6b6,#d6a65a 45%,#4f6a3a)}

/* pagination */
.pager{position:absolute;top:2197px;left:0;width:1200px;display:flex;justify-content:center;gap:4px}
.pager span{width:29px;height:29px;border-radius:50%;border:1px solid #ddd;font-size:10px;color:#666;display:flex;align-items:center;justify-content:center}
.pager span.is-current{border-color:var(--purple);color:var(--purple)}

/* newsletter band */
.band{position:absolute;left:0;top:2288px;width:1200px;height:81px;background:var(--band)}
.band-divider{position:absolute;left:637px;top:0;width:1px;height:81px;background:#dcdcdc}
.newsletter{position:absolute;left:172px;top:22px;display:flex;align-items:center;gap:14px}
.band-label{font-size:16px;font-weight:500;color:var(--ink);line-height:19px}
.subscribe-form{position:relative;width:270px;height:32px;border-radius:16px;background:var(--white);margin-left:18px;font-size:12px;color:#999;line-height:32px;padding-left:16px}
.subscribe-form b{position:absolute;right:0;top:0;width:100px;height:32px;border-radius:16px;background:var(--green);color:var(--white);font-weight:500;text-align:center}
.referral{position:absolute;left:684px;top:22px;width:344px;display:flex;align-items:center;gap:16px}
.referral .band-label{flex:1}

/* footer */
.site-footer{position:absolute;left:0;top:2369px;width:1200px;height:383px;background:var(--purple);color:var(--white)}
.foot-col{position:absolute;top:44px;font-size:12.5px;line-height:19px}
.foot-col h3{font-size:16px;font-weight:500;margin-bottom:12px}
.foot-col p+p{margin-top:12px}
.col-contact{left:172px}
.col-hours{left:393px;width:200px}
.col-tweets{left:611px;width:210px}
.tweet{display:flex;gap:8px;margin-bottom:18px}
.tweet i{width:44px;height:44px;border-radius:50%;background:#b9a7cf;flex:none}
.tweet-meta{display:flex;gap:24px;align-items:center}
.tweet-meta svg{width:11px;height:11px}
.foot-book{position:absolute;left:172px;top:200px;width:186px;height:36px;border-radius:18px;background:var(--green);font-size:13px;font-weight:500;display:flex;align-items:center;justify-content:center;gap:8px}
.badge{position:absolute;left:878px;top:44px;width:104px;height:118px;border-radius:8px;background:var(--orange)}
.badge-note{position:absolute;left:828px;top:178px;width:200px;text-align:center;font-size:12.5px;line-height:19px}
.social{position:absolute;top:290px;left:0;width:1200px;display:flex;justify-content:center;gap:8px}
.social span{width:38px;height:38px;border-radius:50%;border:2px solid var(--white)}
.copyright{position:absolute;left:0;top:350px;width:1200px;text-align:center;font-size:12px}
</style>
</head>
<body>

<header class="site-header">
  <a class="brand" href="#"><span class="brand-dot"></span><span class="brand-name">Thornleigh Vitality Centre<small>Call 416-555-0187</small></span></a>
  <div class="header-cta">
    <a class="pill pill-call" href="#"><svg viewBox="0 0 16 16"><path d="M3 1l3 3-2 2c1 2 3 4 5 5l2-2 3 3-2 3C7 15 1 9 0 4z" fill="#fff"/></svg>Call Us : 416-555-0187</a>
    <a class="pill pill-book" href="#"><svg viewBox="0 0 16 16"><rect x="1" y="3" width="14" height="11" rx="2" fill="none" stroke="#fff" stroke-width="1.6"/><path d="M1 7h14" stroke="#fff" stroke-width="1.6"/></svg>Book An Appointment</a>
  </div>
</header>

<nav class="main-nav">
  <ul>
    <li>Home</li><li>Fees &amp; Services</li><li>Our Staff</li><li>Bios</li>
    <li class="is-active">News &amp; Updates</li><li>Corporate Wellness</li><li>Forms</li><li>Contact</li>
  </ul>
  <div class="search"><svg width="11" height="11" viewBox="0 0 12 12"><circle cx="5" cy="5" r="4" fill="none" stroke="#aaa" stroke-width="1.4"/><path d="M8 8l3 3" stroke="#aaa" stroke-width="1.4"/></svg>Search</div>
</nav>

<section class="hero">
  <svg width="1200" height="298" viewBox="0 0 1200 298">
    <defs>
      <linearGradient id="heroSky" x1="0" y1="0" x2="1" y2="0">
        <stop offset="0" stop-color="#f4f6f8"/>
        <stop offset=".5" stop-color="#e8eef2"/>
        <stop offset=".7" stop-color="#d9c2ad"/>
        <stop offset="1" stop-color="#c9d4dc"/>
      </linearGradient>
    </defs>
    <rect width="1200" height="298" fill="url(#heroSky)" role="img" aria-label="Two smiling runners jogging outdoors in bright morning light"/>
    <path d="M0,228 C250,300 500,300 650,298 C850,296 1050,270 1200,250 L1200,298 L0,298 Z" fill="#fff"/>
    <path d="M0,188 C200,260 450,292 650,296 C450,300 200,290 0,228 Z" fill="#acd036"/>
    <path d="M650,296 C850,290 1050,260 1200,226 L1200,250 C1050,272 850,296 650,298 Z" fill="#886aae"/>
  </svg>
  <div class="hero-title"><span></span><h1>News &amp; Updates</h1></div>
</section>

<main class="posts">
  <article class="post">
    <p class="post-date">30 August 2017</p>
    <h2 class="post-title">Awesome Professional lorem ipsum generator for typographers</h2>
    <div class="post-body">
      <div class="post-photo photo-yoga" role="img" aria-label="Woman doing a yoga stretch on grass at sunrise under palm trees"></div>
      <div class="post-text">
        <p>Class aptent taciti sociosqu ad litora torquent per conubia nostra, per inceptos himenaeos. Mauris in erat justo. Nullam ac urna eu felis dapibus condimentum sit amet a augue. Sed non neque elit. Sed ut imperdiet nisi. Proin condimentum well fermentum nunc. Etiam pharetra, erat sed fermentum feugiat, velit mauris egestas quam, ut aliquam massa nisl quis neque. Suspendisse in orci enim.</p>
        <p>Class aptent taciti sociosqu ad litora torquent per conubia nostra, per inceptos himenaeos. Mauris in erat justo. Nullam ac urna eu felis dapibus condimentum sit amet a augue. Sed non neque elit. Sed ut imperdiet nisi.</p>
        <a class="learn-more" href="#">Learn More →</a>
      </div>
    </div>
  </article>
  <article class="post">
    <p class="post-date">30 August 2017</p>
    <h2 class="post-title">Awesome Professional lorem ipsum generator for typographers</h2>
    <div class="post-body">
      <div class="post-photo photo-rehab" role="img" aria-label="Therapist guiding an older man through a resistance band exercise"></div>
      <div class="post-text">
        <p>Class aptent taciti sociosqu ad litora torquent per conubia nostra, per inceptos himenaeos. Mauris in erat justo. Nullam ac urna eu felis dapibus condimentum sit amet a augue. Sed non neque elit. Sed ut imperdiet nisi. Proin condimentum well fermentum nunc. Etiam pharetra, erat sed fermentum feugiat, velit mauris egestas quam, ut aliquam massa nisl quis neque. Suspendisse in orci enim.</p>
        <p>Class aptent taciti sociosqu ad litora torquent per conubia nostra, per inceptos himenaeos. Mauris in erat justo. Nullam ac urna eu felis dapibus condimentum sit amet a augue. Sed non neque elit. Sed ut imperdiet nisi.</p>
        <a class="learn-more" href="#">Learn More →</a>
      </div>
    </div>
  </article>
  <article class="post">
    <p class="post-date">30 August 2017</p>
    <h2 class="post-title">Awesome Professional lorem ipsum generator for typographers</h2>
    <div class="post-body">
      <div class="post-photo photo-gym" role="img" aria-label="Women running on treadmills in a sunlit gym"></div>
      <div class="post-text">
        <p>Class aptent taciti sociosqu ad litora torquent per conubia nostra, per inceptos himenaeos. Mauris in erat justo. Nullam ac urna eu felis dapibus condimentum sit amet a augue. Sed non neque elit. Sed ut imperdiet nisi. Proin condimentum well fermentum nunc. Etiam pharetra, erat sed fermentum feugiat, velit mauris egestas quam, ut aliquam massa nisl quis neque. Suspendisse in orci enim.</p>
        <p>Class aptent taciti sociosqu ad litora torquent per conubia nostra, per inceptos himenaeos. Mauris in erat justo. Nullam ac urna eu felis dapibus condimentum sit amet a augue. Sed non neque elit. Sed ut imperdiet nisi.</p>
        <a class="learn-more" href="#">Learn More →</a>
      </div>
    </div>
  </article>
  <article class="post">
    <p class="post-date">30 August 2017</p>
    <h2 class="post-title">Awesome Professional lorem ipsum generator for typographers</h2>
    <div class="post-body">
      <div class="post-photo photo-stretch" role="img" aria-label="Physiotherapist stretching a client's leg on a treatment table"></div>
      <div class="post-text">
        <p>Class aptent taciti sociosqu ad litora torquent per conubia nostra, per inceptos himenaeos. Mauris in erat justo. Nullam ac urna eu felis dapibus condimentum sit amet a augue. Sed non neque elit. Sed ut imperdiet nisi. Proin condimentum well fermentum nunc. Etiam pharetra, erat sed fermentum feugiat, velit mauris egestas quam, ut aliquam massa nisl quis neque. Suspendisse in orci enim.</p>
        <p>Class aptent taciti sociosqu ad litora torquent per conubia nostra, per inceptos himenaeos. Mauris in erat justo. Nullam ac urna eu felis dapibus condimentum sit amet a augue. Sed non neque elit. Sed ut imperdiet nisi.</p>
        <a class="learn-more" href="#">Learn More →</a>
      </div>
    </div>
  </article>
  <article class="post">
    <p class="post-date">30 August 2017</p>
    <h2 class="post-title">Awesome Professional lorem ipsum generator for typographers</h2>
    <div class="post-body">
      <div class="post-photo photo-run" role="img" aria-label="Couple jogging along a sunny trail"></div>
      <div class="post-text">
        <p>Class aptent taciti sociosqu ad litora torquent per conubia nostra, per inceptos himenaeos. Mauris in erat justo. Nullam ac urna eu felis dapibus condimentum sit amet a augue. Sed non neque elit. Sed ut imperdiet nisi. Proin condimentum well fermentum nunc. Etiam pharetra, erat sed fermentum feugiat, velit mauris egestas quam, ut aliquam massa nisl quis neque. Suspendisse in orci enim.</p>
        <p>Class aptent taciti sociosqu ad litora torquent per conubia nostra, per inceptos himenaeos. Mauris in erat justo. Nullam ac urna eu felis dapibus condimentum sit amet a augue. Sed non neque elit. Sed ut imperdiet nisi.</p>
        <a class="learn-more" href="#">Learn More →</a>
      </div>
    </div>
  </article>
</main>

<nav class="pager">
  <span>‹</span><span class="is-current">01</span><span>02</span><span>03</span><span>04</span><span>05</span><span>›</span>
</nav>

<section class="band">
  <div class="newsletter">
    <svg width="32" height="28" viewBox="0 0 32 28"><rect x="2" y="8" width="28" height="18" fill="none" stroke="#444" stroke-width="1.6"/><path d="M2 8l14 10 14-10M6 8V2h20v6" fill="none" stroke="#444" stroke-width="1.6"/></svg>
    <span class="band-label">Subscribe<br>Newsletter</span>
    <div class="subscribe-form">Email Address<b>Subscribe</b></div>
  </div>
  <div class="band-divider"></div>
  <div class="referral">
    <svg width="36" height="32" viewBox="0 0 36 32"><rect x="2" y="4" width="24" height="26" fill="none" stroke="#444" stroke-width="1.6"/><path d="M7 12h14M7 18h14M7 24h9M24 2l8 8-10 10h-6v-6z" fill="none" stroke="#444" stroke-width="1.6"/></svg>
    <span class="band-label">Ask one of our associates about our Referral Reward Program!</span>
    <svg width="26" height="16" viewBox="0 0 26 16"><path d="M0 8h24M17 1l7 7-7 7" fill="none" stroke="#333" stroke-width="2"/></svg>
  </div>
</section>

<footer class="site-footer">
  <div class="foot-col col-contact">
    <h3>Contact Us</h3>
    <p>Thornleigh Vitality Centre<br>48 Alder Crescent East, Suite 210<br>Toronto, Ontario, M5X 2K9</p>
    <p>Phone: 416-555-0187<br>Fax: 416-555-0142</p>
  </div>
  <a class="foot-book" href="#"><svg width="13" height="13" viewBox="0 0 16 16"><rect x="1" y="3" width="14" height="11" rx="2" fill="none" stroke="#fff" stroke-width="1.6"/><path d="M1 7h14" stroke="#fff" stroke-width="1.6"/></svg>Book An Appointment</a>
  <div class="foot-col col-hours">
    <h3>Hours of Operation</h3>
    <p>We are open for business at 7:30 am. Open 7 days a week!</p>
    <p>Monday to Friday:<br>7:30am - 8pm</p>
    <p>Saturday to Sunday:<br>10am - 5pm</p>
  </div>
  <div class="foot-col col-tweets">
    <h3>Our Tweets</h3>
    <div class="tweet"><i></i><div>Thornleigh Vitality<br>@ThornleighVital<br>http://short.example/4kd92Lm<div class="tweet-meta">30 Aug 2017<svg viewBox="0 0 12 12"><path d="M6 11L1 6a3 3 0 015-4 3 3 0 015 4z" fill="none" stroke="#fff"/></svg></div></div></div>
    <div class="tweet"><i></i><div>Thornleigh Vitality<br>@ThornleighVital<br>http://short.example/4kd92Lm<div class="tweet-meta">30 Aug 2017<svg viewBox="0 0 12 12"><path d="M6 11L1 6a3 3 0 015-4 3 3 0 015 4z" fill="none" stroke="#fff"/></svg></div></div></div>
  </div>
  <div class="badge" role="img" aria-label="Community choice award badge"></div>
  <p class="badge-note">Thornleigh Vitality Centre is ranked as a top Wellness Centre in Toronto ON<br>Verified by Bookivo.example</p>
  <div class="social"><span aria-label="Chirpline"></span><span aria-label="Circlenet"></span></div>
  <p class="copyright">Copyright © 2017 Thornleigh Vitality Centre</p>
</footer>

</body>
</html>
```